Local Newspaper Quarterly " Meet The Realtor" print ad

I need a new add made up. This was my last ad:
http://www.harborlinepressads.example/static/pdfs/agents1309/Ar092213%20G10%20006%20Prepress.pdf

I do not really care of Realtor advertisements because they are just so cheesy and rather pompous-like. However, it's a necessary evil
My ads have always been outside of the box and/or visually sharp.
I now have a new company' Voske Real Estate( I will attach a logo) contact info:
Carl Voske
Voske Real Estate
Broker/Owner( this can be somewhere in small print or corner of ad since it's mandatory to have shown
Phone: 304-555-0194
Email: Carl@VoskeRealEstate.Example
VoskeRealEstate.Example
I would like social icons(FL,Chirpr, Pinmosaic! Dwello, Qlink)

Ideas: In my logo font or using the image at the top I envision
Something like:
A
Voske Real Estate
Of Mind
Body of ad?
Images of Charleston WV as a real light back ground
With 3 or 4 customer reviews chosen by you in this site:
http://webcarl.example/think.html

Bottom: contact info and my name in a nice Signature style ??
My agent pic at the bottom right( to be small. I don't want my big head overshadowing the message)

I have yet to think of a tagline for my new company:
I have been thinking of " Luxury Services For All Things Real Estate"

Or nothing at all ??? I don't care for tag lines but then again that's part of the business

Target Market(s)

Higher end homes

Industry/Entity Type

Business

Colors
0f59a5
0392cd
0f0f0f
eaeaea
ffffff

Requirements
Must have
• My logo and colors
Nice to have
• My agent picture and client review.
Should not have
• No typical real estate images like a house or home buyer

```html
<!DOCTYPE html>
<html lang="en">
<head>
<meta charset="utf-8">
<title>Voske Real Estate – Meet The Realtor</title>
<link rel="stylesheet" href="https://fonts.googleapis.com/css2?family=Arimo:wght@400;700&family=Great+Vibes&family=Montserrat:ital,wght@1,600&family=Open+Sans:wght@700&display=swap">
<style>
  :root {
    --brand-blue: #0f59a5;
    --sky-blue: #0392cd;
    --ink: #0f0f0f;
    --mist: #eaeaea;
    --white: #ffffff;
    --panel-dark: #2b2b2b;
    --navy-type: #14324f;
  }
  * { box-sizing: border-box; margin: 0; padding: 0; }
  html, body { width: 1200px; height: 913px; overflow: hidden; background: var(--white); }
  .ad { position: relative; width: 1200px; height: 913px; overflow: hidden; font-family: "Montserrat", sans-serif; }

  .city-backdrop {
    position: absolute; inset: 0;
    background: linear-gradient(180deg, #eef1f4 0%, #e4e6e8 20%, #d9d6d2 45%, #dcdad6 60%, #e2e6e6 75%, #d8dcdc 100%);
  }

  .header-band {
    position: absolute; left: 0; top: 0; width: 1200px; height: 92px;
    background: linear-gradient(180deg, var(--sky-blue) 0%, #1a9fd6 60%, #0a86c2 100%);
    border-bottom: 4px solid #bfe3f3;
  }
  .tagline {
    position: absolute; left: 428px; top: 28px;
    font-family: "Arimo", sans-serif; font-weight: 700; font-size: 36px;
    font-variant: small-caps; color: var(--white); letter-spacing: 0.5px; line-height: 1;
  }

  .logo-plate {
    position: absolute; left: 22px; top: 0; width: 368px; height: 184px;
    background: linear-gradient(180deg, #3a3a3a, var(--panel-dark));
    border-radius: 0 0 18px 18px;
    display: flex; align-items: center; justify-content: center;
  }
  .logo-name {
    font-family: "Arimo", sans-serif; font-weight: 700; font-size: 30px;
    color: var(--white); letter-spacing: 3px; text-align: center; line-height: 1.15;
  }

  .review {
    position: absolute; height: 134px;
    background: rgba(255,255,255,0.55);
    border: 1px solid rgba(140,140,140,0.35);
    border-radius: 70px;
    box-shadow: 0 1px 4px rgba(0,0,0,0.12);
  }
  .review-name {
    position: absolute; font-family: "Open Sans", sans-serif; font-weight: 700;
    font-size: 21px; color: var(--ink); letter-spacing: -0.3px; white-space: nowrap;
  }
  .review-text {
    position: absolute; font-style: italic; font-weight: 600; font-size: 15.5px;
    line-height: 19px; color: var(--ink);
  }
  .chat-badge { position: absolute; width: 88px; height: 88px; }

  .contact-strip {
    position: absolute; left: 0; top: 703px; width: 790px; height: 112px;
    background: linear-gradient(180deg, #f2f2f2, var(--mist));
    border-top: 2px solid #cfcfcf;
  }
  .site-url {
    position: absolute; left: 22px; top: 724px;
    font-family: "Arimo", sans-serif; font-weight: 700; font-size: 31px;
    font-variant: small-caps; color: #1d2a1a; letter-spacing: 0.3px;
  }
  .email {
    position: absolute; left: 22px; top: 765px;
    font-family: "Arimo", sans-serif; font-size: 28px; color: #333; letter-spacing: 0.5px;
  }
  .social-list {
    position: absolute; left: 484px; top: 738px; width: 270px;
    display: grid; grid-template-columns: 1fr 1fr; row-gap: 14px; column-gap: 10px;
    list-style: none;
  }
  .social-item {
    display: flex; align-items: center; gap: 7px;
    font-family: "Arimo", sans-serif; font-weight: 700; font-size: 17px; color: var(--brand-blue);
  }
  .social-item::before {
    content: ""; width: 18px; height: 18px; border-radius: 4px; background: var(--brand-blue);
  }

  .phone-band {
    position: absolute; left: 0; top: 815px; width: 790px; height: 98px;
    background: linear-gradient(180deg, #1aa0d8, var(--sky-blue));
  }
  .phone {
    position: absolute; left: 38px; top: 822px;
    font-family: "Arimo", sans-serif; font-weight: 700; font-size: 84px;
    color: var(--navy-type); letter-spacing: 11px; line-height: 1; white-space: nowrap;
    -webkit-text-stroke: 3px #7cc8ea; paint-order: stroke fill;
  }

  .agent-panel {
    position: absolute; left: 785px; top: 714px; width: 415px; height: 199px;
    background: linear-gradient(180deg, #333, var(--panel-dark));
    border-radius: 10px 0 0 0;
  }
  .agent-photo {
    position: absolute; left: 791px; top: 719px; width: 150px; height: 190px;
    background: linear-gradient(160deg, #b5762e 0%, #8a5a2a 35%, #c9b8a8 70%, #a9b4c2 100%);
    border: 2px solid #e0e0e0;
  }
  .signature {
    position: absolute; left: 968px; top: 752px;
    font-family: "Great Vibes", cursive; font-size: 48px; color: var(--white);
    transform: rotate(-10deg); transform-origin: left center; white-space: nowrap; word-spacing: 6px;
  }
  .agent-company {
    position: absolute; left: 940px; width: 260px; top: 843px; text-align: center;
    font-family: "Arimo", sans-serif; font-weight: 700; font-size: 19px; color: var(--white);
  }
  .agent-title {
    position: absolute; left: 940px; width: 260px; top: 872px; text-align: center;
    font-family: "Arimo", sans-serif; font-size: 19px; color: var(--mist);
  }
</style>
</head>
<body>
<main class="ad">
  <div class="city-backdrop" role="img" aria-label="Faded photograph of a downtown city skyline along a river with a bridge"></div>

  <header>
    <div class="header-band"></div>
    <p class="tagline">Luxury Services For All Things Real Estate</p>
    <div class="logo-plate">
      <p class="logo-name">VOSKE<br>REAL ESTATE</p>
    </div>
  </header>

  <svg width="0" height="0" style="position:absolute">
    <defs>
      <radialGradient id="leaf-fill" cx="40%" cy="35%" r="70%">
        <stop offset="0%" stop-color="#9bd66a"/>
        <stop offset="100%" stop-color="#5c9e2e"/>
      </radialGradient>
      <symbol id="chat-icon" viewBox="0 0 88 88">
        <circle cx="44" cy="44" r="43" fill="#dcdcdc" stroke="#c4c4c4"/>
        <circle cx="44" cy="44" r="34" fill="url(#leaf-fill)"/>
        <rect x="28" y="28" width="26" height="20" rx="3" fill="none" stroke="#fff" stroke-width="3"/>
        <path d="M34 54 h22 a3 3 0 0 0 3 -3 v-17 a3 3 0 0 0 -3 -3" fill="none" stroke="#fff" stroke-width="3"/>
        <path d="M36 54 l4 6 l3 -6" fill="none" stroke="#fff" stroke-width="3" stroke-linejoin="round"/>
      </symbol>
    </defs>
  </svg>

  <section class="reviews">
    <article class="review" style="left:645px; top:172px; width:510px;"></article>
    <h3 class="review-name" style="left:700px; top:191px;">Paula Torrance</h3>
    <p class="review-text" style="left:702px; top:228px; width:325px;">Carl was personable and energetic. In the end he got the job done! Thank you Carl!</p>
    <svg class="chat-badge" style="left:1051px; top:196px;"><use href="#chat-icon"/></svg>

    <article class="review" style="left:10px; top:223px; width:510px;"></article>
    <h3 class="review-name" style="left:60px; top:243px;">Raymond D. Blair</h3>
    <p class="review-text" style="left:60px; top:272px; width:340px;">Carl was fantastic. He knew exactly what I was looking for and found the absolute perfect house for me. Truly an asset to his company!</p>
    <svg class="chat-badge" style="left:413px; top:246px;"><use href="#chat-icon"/></svg>

    <article class="review" style="left:523px; top:360px; width:502px;"></article>
    <h3 class="review-name" style="left:573px; top:375px;">Joel and Karen Blayne</h3>
    <p class="review-text" style="left:574px; top:404px; width:340px;">Carl was great! We expected our house to be on the market for awhile but 3 months was much quicker than we anticipated (even though it left us homeless!) Great job!</p>
    <svg class="chat-badge" style="left:926px; top:381px;"><use href="#chat-icon"/></svg>

    <article class="review" style="left:45px; top:519px; width:510px;"></article>
    <h3 class="review-name" style="left:93px; top:538px;">Donna Jarvis</h3>
    <p class="review-text" style="left:94px; top:568px; width:345px;">I could not have asked for more support in my home search. I have already recommended Carl to a few people thinking about buying a new home.</p>
    <svg class="chat-badge" style="left:450px; top:541px;"><use href="#chat-icon"/></svg>

    <article class="review" style="left:675px; top:534px; width:520px;"></article>
    <h3 class="review-name" style="left:723px; top:548px;">Sandra DeLorne Huntington,WV</h3>
    <p class="review-text" style="left:725px; top:581px; width:345px;">Carl is a great asset to your company. I have already given his name to several new Doctors moving to the area that are joining us at Ridgeview University physicians and surgeons!</p>
    <svg class="chat-badge" style="left:1078px; top:556px;"><use href="#chat-icon"/></svg>
  </section>

  <footer>
    <div class="contact-strip"></div>
    <p class="site-url">VoskeRealEstate.Example</p>
    <p class="email">Carl@VoskeRealEstate.Example</p>
    <ul class="social-list">
      <li class="social-item">FL</li>
      <li class="social-item">Chirpr</li>
      <li class="social-item">Pinmosaic</li>
      <li class="social-item">Qlink</li>
    </ul>

    <div class="phone-band"></div>
    <p class="phone">304-555-0194</p>

    <div class="agent-panel"></div>
    <div class="agent-photo" role="img" aria-label="Portrait photograph of the broker, Carl Voske, in front of autumn foliage"></div>
    <p class="signature">Carl Voske</p>
    <p class="agent-company">VOSKE REAL ESTATE</p>
    <p class="agent-title">Broker/Owner</p>
  </footer>
</main>
</body>
</html>
```